I am looking for a modern, clean and neat design for a reflexology and well being business. The business name is Mira Tellus (this is an old Latin word for wellbeing). The colours I would like are purple, white and grey. I am open to suggestions for pictures such as healing or working hands, a pair of feet, images that represent my business that you may think of....... or maybe you think no images at all would be best? My tag line is: "Relax, Renew, Revive" or "Find you balance......... Relax, Renew, Revive" I can decide which I want so I would like to see what both would look like. I would like space on the back to write the client's appointment date and time (more than once)

```html
<!DOCTYPE html>
<html lang="en">
<head>
<meta charset="UTF-8">
<title>Mira Tellus – Business Card</title>
<link href="https://fonts.googleapis.com/css2?family=Lato:ital,wght@0,300;0,400;0,700;1,300;1,400&display=swap" rel="stylesheet">
<style>
  :root {
    --backdrop: #e6e4e6;
    --card-white: #ffffff;
    --lilac: #c6b5c9;
    --charcoal: #2f2c2b;
    --citron: #e5e22a;
    --ink: #2a2a2a;
    --ink-soft: #555257;
    --contact-text: #e8e6e8;
  }
  * { margin: 0; padding: 0; box-sizing: border-box; }
  html, body {
    width: 1200px;
    height: 863px;
    overflow: hidden;
    background: var(--backdrop);
    font-family: "Lato", sans-serif;
  }
  .stage {
    width: 1200px;
    height: 863px;
    display: flex;
    justify-content: center;
    align-items: center;
    gap: 60px;
  }
  .card {
    width: 300px;
    height: 525px;
    background: var(--card-white);
    box-shadow: 0 6px 18px rgba(0, 0, 0, 0.12);
    overflow: hidden;
    position: relative;
  }

  /* Front */
  .card--front {
    display: flex;
    flex-direction: column;
    align-items: center;
    justify-content: center;
    padding-bottom: 40px;
  }
  .brand-name {
    font-weight: 400;
    font-size: 40px;
    color: var(--lilac);
    letter-spacing: 0.5px;
    line-height: 1;
  }
  .brand-tagline {
    margin-top: 6px;
    font-weight: 300;
    font-size: 19px;
    color: var(--ink-soft);
  }

  /* Back */
  .card--back {
    display: flex;
    flex-direction: column;
  }
  .appointment {
    height: 165px;
    background: var(--lilac);
    padding: 24px 22px 0;
  }
  .appointment-label {
    font-weight: 300;
    font-style: italic;
    font-size: 21px;
    color: var(--ink);
    padding: 0 0 4px 6px;
    border-bottom: 1px solid var(--ink-soft);
  }
  .appointment-line {
    height: 40px;
    border-bottom: 1px solid var(--ink-soft);
  }
  .identity {
    height: 60px;
    padding: 12px 26px 0;
    background: var(--card-white);
  }
  .identity-name {
    font-weight: 700;
    font-size: 21px;
    color: var(--ink);
    line-height: 1;
  }
  .identity-role {
    font-weight: 300;
    font-style: italic;
    font-size: 15px;
    color: var(--ink-soft);
  }
  .contacts {
    height: 220px;
    background: var(--charcoal);
    list-style: none;
    padding: 30px 26px 0;
    display: flex;
    flex-direction: column;
    gap: 22px;
  }
  .contact {
    display: flex;
    align-items: center;
    gap: 10px;
    font-size: 14px;
    color: var(--contact-text);
    line-height: 1.05;
  }
  .contact-icon {
    width: 24px;
    height: 24px;
    flex: none;
    background: var(--lilac);
    border-radius: 3px;
    display: flex;
    align-items: center;
    justify-content: center;
  }
  .contact-icon svg { width: 16px; height: 16px; }
  .accent-band {
    flex: 1;
    background: var(--citron);
  }
</style>
</head>
<body>
<main class="stage">
  <section class="card card--front" aria-label="Card front">
    <h1 class="brand-name">Mira Tellus</h1>
    <p class="brand-tagline">Relax, Renew, Revive</p>
  </section>

  <section class="card card--back" aria-label="Card back">
    <div class="appointment">
      <p class="appointment-label">Your next appointment:</p>
      <div class="appointment-line"></div>
      <div class="appointment-line"></div>
    </div>
    <div class="identity">
      <p class="identity-name">JANE DOE</p>
      <p class="identity-role">Owner</p>
    </div>
    <ul class="contacts">
      <li class="contact">
        <span class="contact-icon">
          <svg viewBox="0 0 16 16"><rect x="1.5" y="3.5" width="13" height="9" fill="#fff"/><path d="M1.5 3.5 L8 9 L14.5 3.5" fill="none" stroke="#c6b5c9" stroke-width="1.2"/></svg>
        </span>
        info@miratellus.com
      </li>
      <li class="contact">
        <span class="contact-icon">
          <svg viewBox="0 0 16 16"><circle cx="8" cy="8" r="6.5" fill="none" stroke="#fff" stroke-width="1.2"/><path d="M5.6 4.6 L6.9 4.4 L7.5 6.2 L6.7 6.9 Q7.4 8.6 9.1 9.3 L9.8 8.5 L11.6 9.1 L11.4 10.4 Q10.8 11.3 9.6 11.1 Q5.4 10 4.9 6.4 Q4.8 5.2 5.6 4.6 Z" fill="#fff"/></svg>
        </span>
        123 456 789
      </li>
      <li class="contact">
        <span class="contact-icon">
          <svg viewBox="0 0 16 16"><path d="M8 14.5 C5 10.5 3.8 8.4 3.8 6.2 A4.2 4.2 0 0 1 12.2 6.2 C12.2 8.4 11 10.5 8 14.5 Z" fill="#fff"/><circle cx="8" cy="6.2" r="1.6" fill="#c6b5c9"/></svg>
        </span>
        <span>Address Line 1<br>Address Line 2</span>
      </li>
    </ul>
    <div class="accent-band"></div>
  </section>
</main>
</body>
</html>
```